Business Card Design needed for start up company Pramora

In need of a new business card designed for a start up company based in Sydney, Pramora is a new start up innovative Company, our mission it to make property accessible for everyday Australian and to become the leading Real Estate platform in Australia. We want it to be fresh and clean.

Industry/Entity Type

Financial

Contact Information for Business Card

Section for Name
Section for Title

PRAMORA - Where Doors Open Wide
Mobile:
Direct:

Font styles to use
Sans Serif

Colors
33a6d7
0692cd
0255a3
ffffff

Requirements
Must have
• Logo, all business card details

```html
<!DOCTYPE html>
<html lang="en">
<head>
<meta charset="UTF-8">
<title>Pramora – Business Card</title>
<link href="https://fonts.googleapis.com/css2?family=Roboto:wght@400;500;900&display=swap" rel="stylesheet">
<style>
  :root {
    --backdrop: #5b6266;
    --sky: #229bd6;
    --navy: #1f4a87;
    --navy-deep: #143766;
    --white: #ffffff;
    --ink: #2a2f36;
  }
  * { box-sizing: border-box; margin: 0; padding: 0; }
  html, body {
    width: 1200px; height: 900px; overflow: hidden;
    background: var(--backdrop);
    font-family: "Roboto", Arial, sans-serif;
  }
  .sheet {
    width: 1200px; height: 900px;
    display: flex; flex-direction: column;
    align-items: center; justify-content: center; gap: 56px;
  }
  .card {
    position: relative;
    width: 620px; height: 354px;
    border-radius: 18px; overflow: hidden;
    background: var(--white);
    box-shadow: 0 14px 30px rgba(0,0,0,.35);
  }
  .card__art { position: absolute; inset: 0; }

  /* front */
  .brand {
    position: absolute; left: 40px; top: 34px;
    display: flex; align-items: center; gap: 8px;
  }
  .brand__dot {
    width: 54px; height: 54px; border-radius: 50%;
    background: var(--sky);
  }
  .brand__name {
    font-weight: 900; font-size: 40px; letter-spacing: -1px;
    color: var(--navy);
  }
  .contacts {
    position: absolute; left: 40px; top: 150px;
    list-style: none; display: flex; flex-direction: column; gap: 9px;
  }
  .contacts li {
    display: flex; align-items: center; gap: 10px;
    font-size: 14px; color: var(--ink);
  }
  .contacts svg { width: 20px; height: 20px; flex: none; }
  .person {
    position: absolute; left: 360px; top: 64px; width: 228px;
    text-align: center; color: var(--white);
  }
  .person__name { font-size: 24px; font-weight: 400; letter-spacing: 1px; }
  .person__title { font-size: 12px; letter-spacing: 1px; margin-top: 4px; }
  .address {
    position: absolute; left: 330px; top: 238px; width: 260px;
    text-align: center; color: var(--white);
    font-size: 15px; line-height: 1.35;
  }

  /* back */
  .card--back { background: var(--sky); }
  .back-brand {
    position: absolute; inset: 0;
    display: flex; align-items: center; justify-content: center; gap: 10px;
  }
  .back-brand__dot {
    width: 96px; height: 96px; border-radius: 50%;
    background: var(--white);
  }
  .back-brand__name {
    font-weight: 900; font-size: 72px; letter-spacing: -2px;
    color: var(--navy);
  }
</style>
</head>
<body>
<main class="sheet">

  <section class="card card--front" aria-label="Business card front">
    <svg class="card__art" viewBox="0 0 620 354" aria-hidden="true">
      <polygon points="340,0 620,0 620,354 235,354" fill="var(--sky)"/>
      <polygon points="348,58 372,46 372,150 348,150" fill="var(--navy-deep)"/>
      <rect x="360" y="46" width="232" height="104" fill="var(--navy)"/>
    </svg>

    <div class="brand">
      <span class="brand__dot"></span>
      <span class="brand__name">PRAMORA</span>
    </div>

    <ul class="contacts">
      <li>
        <svg viewBox="0 0 20 20"><rect width="20" height="20" rx="2" fill="var(--navy)"/><path d="M6 4.5l2.2 2.4-1.1 1.6c.8 1.7 2 2.9 3.6 3.7l1.5-1.1 2.4 2.2-1.3 1.9C9.400 15 5 10.6 4.6 5.8z" fill="var(--white)"/></svg>
        555-014-2736
      </li>
      <li>
        <svg viewBox="0 0 20 20"><rect width="20" height="20" rx="2" fill="var(--navy)"/><rect x="6.5" y="3.5" width="7" height="13" rx="1.2" fill="none" stroke="var(--white)" stroke-width="1.4"/><circle cx="10" cy="14" r=".9" fill="var(--white)"/></svg>
        555-019-8821
      </li>
      <li>
        <svg viewBox="0 0 20 20"><rect width="20" height="20" rx="2" fill="var(--navy)"/><rect x="4" y="6" width="12" height="8.5" fill="none" stroke="var(--white)" stroke-width="1.3"/><path d="M4 6l6 5 6-5" fill="none" stroke="var(--white)" stroke-width="1.3"/></svg>
        hello@pramora.au
      </li>
      <li>
        <svg viewBox="0 0 20 20"><rect width="20" height="20" rx="2" fill="var(--navy)"/><circle cx="10" cy="10" r="5.5" fill="none" stroke="var(--white)" stroke-width="1.3"/><path d="M4.5 10h11M10 4.5c-2.4 3-2.4 8 0 11M10 4.5c2.4 3 2.4 8 0 11" fill="none" stroke="var(--white)" stroke-width="1"/></svg>
        www.pramora.au
      </li>
    </ul>

    <div class="person">
      <p class="person__name">LIAM HARTWELL</p>
      <p class="person__title">OWNER</p>
    </div>

    <p class="address">48 Harbour Lane, Suite 210<br>Sydney, NSW 2000</p>
  </section>

  <section class="card card--back" aria-label="Business card back">
    <div class="back-brand">
      <span class="back-brand__dot"></span>
      <span class="back-brand__name">PRAMORA</span>
    </div>
  </section>

</main>
</body>
</html>
```